Financial services business - Brochure Design

Existing financial services company in Melbourne, Australia needing a brochure design. We have an idea for the type of layout we want, but looking to the designer to help realize it.
We want the brochure to convey how professional we are and for the reader to feel trust and security.
The service this brochure covers is around a concept of Quiet Harvest - i.e. how to get rich without thinking about it.

I've attached two documents:
1) QuietHarvest.doc - this is the content for the brochure with some rough drawings and diagrams. The drawings are only rough ideas of the way I want to represent the content. Please re-draw these but theme them consistently.
2) KMHoldings design(concept).doc - this is another rough design we had drafted up in the past that never went through for design. I've included this as an indication as to how we'd like this done and ideas like emphasising certain phrases on colourful sections or whole blank pages to draw attention to phrases or sentences for the reader.

Specifications:
- Communicate wealth, growth, security/safety and trustworthiness.
- Design to be ready to print professionally.
- Please include some stock imagery as appropriate/ where appropriate.
- Please include soft copy that can be distributed in say for example, *.pdf format.
- Original design files required so we can make alterations if required.

```html
<!DOCTYPE html>
<html lang="en">
<head>
<meta charset="utf-8">
<title>Quiet Harvest – Brochure Spread</title>
<link rel="stylesheet" href="https://fonts.googleapis.com/css2?family=Roboto:wght@300;400&family=Roboto+Condensed:wght@300;400;700&display=swap">
<style>
  :root {
    --backdrop: #8a8a8a;
    --paper: #ffffff;
    --ink: #2b2b2b;
    --brand-blue: #1d3a8f;
    --sky-top: #5d84bf;
    --sky-mid: #4a74b6;
    --sky-low: #5a86c8;
    --night-top: #3f6aab;
    --night-mid: #2b4a80;
    --night-low: #14233f;
    --white: #ffffff;
  }
  * { box-sizing: border-box; margin: 0; padding: 0; }
  html, body {
    width: 1200px; height: 829px; overflow: hidden;
    background: var(--backdrop);
  }
  .spread {
    position: absolute; left: 20px; top: 33px;
    width: 1160px; height: 749px;
    display: flex;
  }
  /* Inside page */
  .page-inside {
    width: 365px; height: 100%;
    background: var(--paper);
    padding: 46px 40px 0 55px;
    font-family: "Roboto Condensed", sans-serif;
    color: var(--ink);
    font-size: 8.6px; line-height: 11.6px; font-weight: 300;
  }
  .section-title {
    font-family: "Roboto", sans-serif; font-weight: 300;
    color: var(--brand-blue); font-size: 19px; line-height: 24px;
    margin-bottom: 9px;
  }
  .section-title + p { margin-bottom: 14px; }
  .benefit-title {
    font-weight: 700; color: var(--brand-blue);
    font-size: 8.8px; margin: 0 0 6px;
  }
  .page-inside p { margin-bottom: 6px; }
  .page-inside p.tight { margin-bottom: 0; }
  .gap { margin-top: 10px; }

  /* Back panel with sky */
  .panel-sky {
    position: relative; width: 215px; height: 100%;
    background: linear-gradient(180deg, var(--sky-top) 0%, var(--sky-mid) 45%, var(--sky-low) 100%);
    color: var(--white);
    font-family: "Roboto Condensed", sans-serif; font-weight: 300;
  }
  .next-steps {
    position: absolute; left: 13px; top: 413px; width: 190px;
    font-size: 11.6px; line-height: 15.3px;
  }
  .next-steps h2 {
    font-family: "Roboto", sans-serif; font-weight: 300;
    font-size: 18px; margin-bottom: 11px;
  }
  .next-steps p { margin-bottom: 15px; }

  /* Cover */
  .page-cover {
    position: relative; flex: 1; height: 100%;
    background:
      radial-gradient(ellipse at 70% 40%, rgba(170,190,230,0.35) 0%, rgba(0,0,0,0) 55%),
      linear-gradient(180deg, var(--night-top) 0%, var(--night-mid) 55%, var(--night-low) 100%);
    color: var(--white);
  }
  .cover-title {
    position: absolute; left: 159px; top: 140px;
    font-family: "Roboto", sans-serif; font-weight: 300;
    font-size: 40px; line-height: 42px; letter-spacing: -0.5px;
  }
  .cover-tagline {
    position: absolute; left: 160px; top: 180px;
    font-family: "Roboto", sans-serif; font-weight: 300;
    font-size: 18px;
  }
  .brand-tile {
    position: absolute; left: 373px; top: 548px;
    width: 135px; height: 134px;
    background: var(--white);
    border-radius: 14px 0 14px 0;
    display: flex; flex-direction: column; align-items: center; justify-content: center;
    gap: 10px;
  }
  .brand-dot {
    width: 38px; height: 38px; border-radius: 50%;
    background: var(--brand-blue);
  }
  .brand-name {
    font-family: "Roboto Condensed", sans-serif; font-weight: 400;
    color: var(--brand-blue); font-size: 15px; letter-spacing: 1px;
    text-align: center; line-height: 18px;
  }
</style>
</head>
<body>
<main class="spread">
  <section class="page-inside">
    <h2 class="section-title">Who uses Quiet Harvest?</h2>
    <p>Individuals and families from varying life stages are able to take advantage of the Quiet Harvest solution. Whether your goal is to save for the first home or pay down your home quicker, invest in property or equities, retire comfortably or combinations of these, there are numerous benefits to be gained.</p>

    <h2 class="section-title">Key benefits</h2>
    <h3 class="benefit-title">Get into your first home faster</h3>
    <p>It’s the Australian dream to own our own home. Quiet Harvest fast tracks the deposit saving process, but also teaches you the discipline that is required when you eventually are required to start making mortgage repayments.</p>
    <h3 class="benefit-title">Automate your finance and save time</h3>
    <p class="tight">There is only so much you can achieve in 24 hours. With more time, you’d be able to get to the gym more often, learn another language, pick up more hobbies or get more sleep. The reality is that by the time you get home from a full day of work, you’d like to put your feet up and wind down with a good book and your favourite bottle of wine - the last thing you want to think about is your finances.</p>
    <p>Quiet Harvest affords you that luxury to relax after a tiring day at the office, whilst knowing your financial goals are being looked after.</p>
    <h3 class="benefit-title">Financial peace of mind</h3>
    <p>Clients often describe the feeling of unease and even guilt following a sporadic purchase, a splurge on an overseas holiday and the lack of proactivity in thinking seriously about their finances. Quiet Harvest allows you and encourages you to reward yourself because your system is quietly working hard to achieve your goals in the background.</p>
    <h3 class="benefit-title">Built-in accountability</h3>
    <p>The quarterly reviews build in an additional layer of accountability over your finances. Having additional sets of eyes look over your financial situation four times per year greatly increases the chances of reaching your goals by keeping you on a disciplined path.</p>

    <h2 class="section-title gap">Additional Benefits</h2>
    <h3 class="benefit-title">Empowered decision making</h3>
    <p>Knowledge and data are paramount in the modern world. Clients who work with us enjoy the additional benefits of having access to our data and subscriptions. Property and stock reports enable our clients to make informed decisions during both the buying and selling stages.</p>
    <h3 class="benefit-title">Access to professionals</h3>
    <p>At KM Holdings Group, our professionals all sit under the one roof. Our clients are able to access their accountant, finance broker and financial planner at the one location. A by-product of having your professionals centrally located is the ability to provide our clients with well-rounded strategies which holistically take into consideration all their circumstances.</p>
  </section>

  <section class="panel-sky" role="img" aria-label="Photograph of a soft blue sky with thin clouds">
    <div class="next-steps">
      <h2>Next Steps</h2>
      <p>Contact us today or visit our website to organise an appointment.<br>
      www.kmholdings.com.au<br>
      42 Larch Street,<br>
      Kewford, VIC 3199</p>
      <p>1300 555 014</p>
      <p>The information contained within this booklet is for general information purposes only. KM Holdings Group Pty Ltd does not accept any liability for any decisions made on the basis of this information. This booklet does not constitute financial advice and should not be taken as such. All examples, figures and data are for illustrative purposes only.</p>
    </div>
  </section>

  <section class="page-cover" role="img" aria-label="Photograph of a man seen from behind on the phone, looking out over a city harbour lit up at dusk">
    <h1 class="cover-title">Quiet Harvest</h1>
    <p class="cover-tagline">The road to financial freedom made easy</p>
    <div class="brand-tile">
      <span class="brand-dot"></span>
      <span class="brand-name">KM HOLDINGS<br>GROUP</span>
    </div>
  </section>
</main>
</body>
</html>
```